Business Card Project

We are a small consulting firm. You can experiment with any design.
Must have:
1) Company name - OLUNDEX International
2) Company slogan - simple solutions for complex problems
3) Name/Title/Phone/Email/WWW/ - use anything you like as an example.

Industry/Entity Type

Business

```html
<!DOCTYPE html>
<html lang="en">
<head>
<meta charset="utf-8">
<title>OLUNDEX International – Business Card</title>
<link rel="stylesheet" href="https://fonts.googleapis.com/css2?family=Arimo:wght@400;700&display=swap">
<style>
  :root {
    --stage: #e9ebef;
    --blue-deep: #0a1d78;
    --blue-mid: #1538b0;
    --blue-name: #1d6fd6;
    --grey-title: #5a5a5a;
    --grey-text: #2b2b2b;
    --card-white: #ffffff;
    --card-silver: #d6d8dc;
    --logo-white: #ffffff;
    --slogan-tint: #c9d7fb;
  }
  * { margin: 0; padding: 0; box-sizing: border-box; }
  html, body { width: 1200px; height: 751px; overflow: hidden; }
  body {
    background: var(--stage);
    font-family: "Arimo", Arial, sans-serif;
  }
  .business-card {
    position: absolute;
    left: 150px;
    top: 132px;
    width: 900px;
    height: 486px;
    border-radius: 34px;
    overflow: hidden;
    display: flex;
    background: linear-gradient(160deg, var(--card-white) 0%, #f2f3f5 55%, var(--card-silver) 100%);
    box-shadow: 0 14px 40px rgba(0, 0, 0, 0.18);
  }
  .brand-panel {
    position: relative;
    width: 440px;
    height: 100%;
    flex-shrink: 0;
    background: linear-gradient(170deg, var(--blue-mid) 0%, var(--blue-deep) 100%);
  }
  .brand-panel__waves {
    position: absolute;
    left: 0;
    right: 0;
    bottom: 0;
    height: 62%;
    background:
      radial-gradient(ellipse 120% 60% at 30% 70%, rgba(120, 170, 255, 0.45) 0%, rgba(47, 111, 230, 0.25) 40%, rgba(10, 29, 120, 0) 75%),
      linear-gradient(180deg, rgba(47, 111, 230, 0) 0%, rgba(47, 111, 230, 0.35) 100%);
  }
  .brand-panel__edge {
    position: absolute;
    top: 0;
    right: 0;
    width: 10px;
    height: 100%;
    background: linear-gradient(90deg, #9fb3e8, #e8ecf6);
  }
  .company-mark {
    position: absolute;
    left: 44px;
    top: 82px;
    display: flex;
    align-items: center;
    gap: 16px;
  }
  .company-mark__dot {
    width: 44px;
    height: 44px;
    border-radius: 50%;
    background: var(--logo-white);
    flex-shrink: 0;
  }
  .company-mark__name {
    color: var(--logo-white);
    font-weight: 400;
    font-size: 30px;
    line-height: 1.1;
    letter-spacing: 0.5px;
  }
  .company-slogan {
    position: absolute;
    left: 44px;
    top: 172px;
    width: 360px;
    color: var(--slogan-tint);
    font-size: 16px;
    letter-spacing: 0.3px;
  }
  .contact-side {
    position: relative;
    flex: 1;
  }
  .person {
    position: absolute;
    right: 40px;
    top: 92px;
    text-align: right;
  }
  .person__name {
    color: var(--blue-name);
    font-size: 42px;
    font-weight: 400;
    line-height: 1.1;
  }
  .person__title {
    color: var(--grey-title);
    font-size: 28px;
    line-height: 1.3;
    margin-top: 2px;
  }
  .details {
    position: absolute;
    right: 40px;
    bottom: 52px;
    text-align: right;
    color: var(--grey-text);
    font-size: 19px;
    line-height: 1.4;
    font-style: normal;
  }
</style>
</head>
<body>
  <main class="business-card">
    <section class="brand-panel">
      <div class="brand-panel__waves" role="img" aria-label="Flowing light-blue wave and snowflake decoration"></div>
      <div class="brand-panel__edge"></div>
      <div class="company-mark">
        <span class="company-mark__dot"></span>
        <span class="company-mark__name">OLUNDEX<br>International</span>
      </div>
      <p class="company-slogan">simple solutions for complex problems</p>
    </section>
    <section class="contact-side">
      <div class="person">
        <h1 class="person__name">Marla Quenby</h1>
        <p class="person__title">Sales Manager</p>
      </div>
      <address class="details">
        <p>Harbor Lane 12</p>
        <p>mob: 041 562 3390</p>
        <p>email: marla@quenby.net</p>
        <p>www.olundexintl.com</p>
      </address>
    </section>
  </main>
</body>
</html>
```